Dr. Plume Southern Reef Oil

We need a bottle label design for a new company called Dr. Plume. We sell krill oil in gel caps. Krill are shrimp-like crustaceans. We are looking for a professional concept that communicates the essence of ocean, health, life, purity...maybe a krill with medical authority.

There are a few labels out there. I attached 2. Dr. Halvorsen has some nice vector krill art, though the label is otherwise sparse. Copper Meadow has the feel of a nice full line of professional products, though there's nothing particularly krilly about it. Could there be a happy marriage of the two?

What we do NOT want is a photograph of an ocean with words over it. That screams Japanese karaoke.

Auxiliary wording on label front:
Heart Health
Antarctic
100% Pure
Dietary Supplements
1000mg

I apologize to designers for my new-to-crowd-design vagueness above, but I will try to be very forthcoming with feedback.

Thank you all!

Target Market(s)

Krill oil buyers. The 40+ crowd who want their Omega 3s and know that krill oil has it in spades!

Requirements
Nice to have
• A singular image that can be lifted for website branding as well...

```html
<!DOCTYPE html>
<html lang="en">
<head>
<meta charset="utf-8">
<title>Dr. Plume – Krill Oil Label</title>
<link rel="stylesheet" href="https://fonts.googleapis.com/css2?family=Open+Sans:wght@400;600;700;800&display=swap">
<style>
  :root{
    --blue:#1a5d9e;
    --blue-deep:#0f4f8f;
    --blue-bright:#1f72c4;
    --orange:#e67a1a;
    --sky:#8ccbeb;
    --pale:#dbeef9;
    --ink:#1d4f86;
    --rule:#cfcfcf;
    --slot:#dcdcdc;
    --paper:#ffffff;
  }
  *{box-sizing:border-box;margin:0;padding:0}
  html,body{width:1200px;height:1000px;overflow:hidden;background:var(--paper)}
  body{position:relative;font-family:"Open Sans",Arial,sans-serif;color:var(--ink)}

  .label-sheet{position:absolute;left:10px;top:18px;width:1178px;height:390px;border:1px solid var(--rule)}

  /* facts panel */
  .facts{position:absolute;left:20px;top:18px;width:250px;height:272px;border:1.5px solid var(--blue);padding:6px 10px;font-size:9.5px;overflow:hidden}
  .facts__title{text-align:center;font-size:17px;line-height:22px;font-weight:800;color:var(--blue);letter-spacing:.3px;margin-bottom:4px}
  .facts__row{display:flex;justify-content:space-between;padding:0 2px;line-height:16px;font-size:9px;white-space:nowrap}
  .facts__bar{height:5px;background:var(--blue);margin:3px 0 8px}
  .facts__list{list-style:none;line-height:17px;padding-left:0}
  .facts__bar--end{height:8px;margin:7px 0 5px}
  .facts__note{font-size:9px;line-height:12px;padding-left:2px;white-space:nowrap}
  .ingredients{position:absolute;left:22px;top:298px;font-size:9.5px;line-height:13px}
  .ingredients b{font-weight:700}
  .side-title{position:absolute;left:77px;top:330px;text-align:center}
  .side-title__main{font-size:24px;line-height:26px;font-weight:700;color:var(--blue)}
  .side-title__main span{font-weight:400}
  .side-title__sub{font-size:10.5px;font-weight:700;color:var(--orange);letter-spacing:1.6px}

  /* front panel */
  .front{position:absolute;width:532px;height:390px;border:1px solid #9aa7b3;background:var(--paper);overflow:hidden}
  .front--label{left:288px;top:0}
  .front--mini{left:78px;top:560px;transform:scale(.55);transform-origin:0 0}
  .brand-square{position:absolute;left:33px;top:0;width:115px;height:89px;background:linear-gradient(135deg,var(--blue-bright),var(--blue-deep));display:flex;align-items:center;justify-content:center;color:#fff;font-weight:700;font-size:22px}
  .pure-badge{position:absolute;left:432px;top:14px;width:80px;height:80px}
  .krill-art{position:absolute;left:5px;top:44px;width:510px;height:172px;background:radial-gradient(ellipse 70px 70px at 52% 48%,var(--orange) 0 96%,var(--pale) 98%,transparent 100%),radial-gradient(ellipse 260px 40px at 50% 72%,var(--sky) 0,rgba(140,203,235,.4) 60%,transparent 100%)}
  .title{position:absolute;left:0;right:0;top:202px;text-align:center;font-size:58px;line-height:62px;font-weight:700;color:var(--blue);letter-spacing:-.5px}
  .title span{font-weight:400}
  .band-blue{position:absolute;left:0;right:0;top:264px;height:30px;background:var(--blue);color:#fff;text-align:center;font-weight:700;font-size:19px;letter-spacing:5px;line-height:30px}
  .band-orange{position:absolute;left:0;right:0;top:294px;height:86px;background:var(--orange)}
  .band-orange__region{position:absolute;left:20px;right:20px;top:4px;display:flex;align-items:center;gap:14px;color:#fff;font-weight:600;font-size:16px;letter-spacing:5px}
  .band-orange__region i{flex:1;height:1px;background:#fff}
  .dietary{position:absolute;left:25px;top:48px;color:#fff;font-weight:800;font-size:21px}
  .dose-tab{position:absolute;right:0;top:42px;width:150px;height:44px}
  .dose-tab span{position:absolute;left:26px;top:6px;color:#fff;font-size:18px}
  .band-foot{position:absolute;left:0;right:0;top:380px;height:10px;background:var(--blue)}

  /* right panel */
  .info{position:absolute;left:835px;top:18px;width:232px;font-size:9.2px;line-height:15px;color:var(--ink)}
  .info p{margin-bottom:8px}
  .info b{font-weight:700}
  .info__box{border:1.5px solid var(--blue);padding:4px 6px;margin-bottom:10px}
  .distributor{position:absolute;left:835px;top:292px;font-size:12px;line-height:23px}
  .code-slot{position:absolute;left:1077px;top:18px;width:85px;height:264px;background:var(--slot)}

  /* brand lockup */
  .lockup-square{position:absolute;left:930px;top:500px;width:231px;height:172px;background:linear-gradient(135deg,var(--blue-bright),var(--blue-deep));display:flex;align-items:center;justify-content:center;color:#fff;font-weight:700;font-size:44px}
  .lockup-art{position:absolute;left:425px;top:630px;width:765px;height:225px;background:radial-gradient(circle 102px at 53% 44%,var(--orange) 0 94%,var(--pale) 96%,transparent 99%),radial-gradient(ellipse 390px 60px at 50% 60%,var(--sky) 0,rgba(140,203,235,.4) 60%,transparent 100%)}
  .lockup-title{position:absolute;left:560px;top:858px;width:510px;text-align:center;font-size:86px;line-height:90px;font-weight:700;color:var(--blue);letter-spacing:-1px}
  .lockup-title span{font-weight:400}
</style>
</head>
<body>

<section class="label-sheet">
  <div class="facts">
    <h2 class="facts__title">SUPPLEMENT FACTS</h2>
    <div class="facts__row"><span>Serving Size : 2 softgels&nbsp; Serving per container : 30</span></div>
    <div class="facts__row"><span>Amount per Serving :</span><span>%DV*</span></div>
    <div class="facts__bar"></div>
    <ul class="facts__list">
      <li>Vitamin A</li>
      <li>Polaris Krill Oil (PKO)</li>
      <li>Phospholipiods, omega -3 rich</li>
      <li>Eicosapentaenoic acid (EPA)</li>
      <li>Docosahexaenoic Acis (DHA)</li>
      <li>Omega-6 fatty acids, total</li>
      <li>Transfat</li>
      <li>Astaxanthin</li>
    </ul>
    <div class="facts__bar facts__bar--end"></div>
    <p class="facts__note">*Percent Daily Values based on a 2,000 calorie diet<br>&nbsp;** Daily Value not established</p>
  </div>
  <p class="ingredients"><b>Other ingredients :</b> Gelatin (capsule),glycerin &amp; water.<br><b>Expiration Date :</b></p>
  <div class="side-title">
    <div class="side-title__main">KRILL <span>OIL</span></div>
    <div class="side-title__sub">HEART HEALTH</div>
  </div>

  <div class="front front--label">
    <div class="brand-square">Dr. Plume</div>
    <svg class="pure-badge" viewBox="0 0 80 80" aria-hidden="true">
      <path d="M52 6 A36 36 0 0 1 44 74" fill="none" stroke="#e67a1a" stroke-width="3"/>
      <text x="38" y="33" text-anchor="middle" font-family="Open Sans,Arial,sans-serif" font-weight="700" font-size="15" fill="#e67a1a">100%</text>
      <text x="36" y="55" text-anchor="middle" font-family="Open Sans,Arial,sans-serif" font-weight="700" font-size="22" fill="#1f72c4">pure</text>
    </svg>
    <div class="krill-art" role="img" aria-label="Krill illustration in an orange circle over pale blue Antarctic mountains"></div>
    <h1 class="title">KRILL <span>OIL</span></h1>
    <div class="band-blue">HEART HEALTH</div>
    <div class="band-orange">
      <div class="band-orange__region"><i></i>ANTARCTIC<i></i></div>
      <div class="dietary">DIETARY SUPPLEMENT</div>
      <div class="dose-tab">
        <svg width="150" height="44" viewBox="0 0 150 44" aria-hidden="true"><path d="M0 44 C14 44 10 0 30 0 H150 V44 Z" fill="#1a5d9e"/></svg>
        <span>1000mg</span>
      </div>
    </div>
    <div class="band-foot"></div>
  </div>

  <div class="info">
    <p><b>Suggested Use</b> : 2 Softgels daily with the first meal.</p>
    <p><b>Warning</b> : If you are allergic to shellfish, have a blood coagulation condition, or are taking anticoagulants sch as Warfarin (Clotrex). Consult a health care professional prior to use.</p>
    <p>PKO is a extract from Antarctical that is rich in cell membrane building blocks : highly unsaturated phosolipids co-functionalized with omega-3 fatty acids (EPA &amp; DHA). Although benifitioual for both men &amp; women, PKO also supports relief of PMS Symptoms.*</p>
    <div class="info__box"><b>Suggested Use</b> : 2 Softgels daily with the first These Statements have been approved by the FDA. This product is not intended to diagnose, treat, Cureor Prevent any disease.</div>
  </div>
  <p class="distributor">Distributed by :<br>customer services @<br>address State pin code<br>Contact : 0000 000 0000</p>
  <div class="code-slot"></div>
</section>

<div class="front front--mini">
  <div class="brand-square">Dr. Plume</div>
  <svg class="pure-badge" viewBox="0 0 80 80" aria-hidden="true">
    <path d="M52 6 A36 36 0 0 1 44 74" fill="none" stroke="#e67a1a" stroke-width="3"/>
    <text x="38" y="33" text-anchor="middle" font-family="Open Sans,Arial,sans-serif" font-weight="700" font-size="15" fill="#e67a1a">100%</text>
    <text x="36" y="55" text-anchor="middle" font-family="Open Sans,Arial,sans-serif" font-weight="700" font-size="22" fill="#1f72c4">pure</text>
  </svg>
  <div class="krill-art" role="img" aria-label="Krill illustration in an orange circle over pale blue Antarctic mountains"></div>
  <div class="title">KRILL <span>OIL</span></div>
  <div class="band-blue">HEART HEALTH</div>
  <div class="band-orange">
    <div class="band-orange__region"><i></i>ANTARCTIC<i></i></div>
    <div class="dietary">DIETARY SUPPLEMENT</div>
    <div class="dose-tab">
      <svg width="150" height="44" viewBox="0 0 150 44" aria-hidden="true"><path d="M0 44 C14 44 10 0 30 0 H150 V44 Z" fill="#1a5d9e"/></svg>
      <span>1000mg</span>
    </div>
  </div>
  <div class="band-foot"></div>
</div>

<div class="lockup-square">Dr. Plume</div>
<div class="lockup-art" role="img" aria-label="Large krill illustration in an orange circle over pale blue Antarctic mountains"></div>
<div class="lockup-title">KRILL <span>OIL</span></div>

</body>
</html>
```